TR Hornets Dunmore (Social Media Pack & Stationary)

Create Stationary Designs as well as Social Media Designs (Twitter, Instagram & Facebook) as well as a Square and Banner Social media template... keep the logo I attached in the Ai file... I would like the blue in the TR Hornets logo to be navy blue instead of the dark blue.

Willing to give a good tip to get it done quicker

Please use the logo provided in the ai file.

Instagram account: @trhdunmore
FB account: TR Hornets Dunmore
Twitter: @trhdunmore

Target Market(s)

Parents and players

Font styles to use
Serif

Colors
0255a3
f78f20
f37122

Requirements
Must have
• Stationary
Twitter & FB heading
Template to post social media announcements
Template for pictures to post on social media
Template to post schedule
Envelop
Business Card
(All must include logo)

```html
<!DOCTYPE html>
<html lang="en">
<head>
<meta charset="utf-8">
<title>TR Hornets Dunmore – Social Media Pack</title>
<link rel="stylesheet" href="https://fonts.googleapis.com/css2?family=Tinos:wght@400;700&family=Arimo:wght@400&display=swap">
<style>
  :root {
    --orange-deep: #ff4f03;
    --orange-mid: #ff6a05;
    --orange-panel: #ff5f05;
    --orange-edge: #ff4a00;
    --red: #ff2504;
    --amber: #fc9504;
    --tangerine: #f27305;
    --logo-blue: #0b1ad6;
    --logo-red: #ff2200;
    --white: #ffffff;
    --ink: #000000;
    --serif: "Tinos", "Times New Roman", serif;
    --sans: "Arimo", Arial, sans-serif;
  }
  * { margin: 0; padding: 0; box-sizing: border-box; }
  html, body { width: 1200px; height: 947px; overflow: hidden; background: var(--white); }
  .canvas { position: relative; width: 1200px; height: 947px; background: var(--white); font-family: var(--serif); }
  .layer { position: absolute; left: 0; top: 0; }

  .brand { position: absolute; font-family: var(--serif); font-weight: 700; line-height: 1; white-space: nowrap; text-align: center; }
  .brand .brand-sub { display: block; }

  .square-brand { left: 172px; top: 100px; width: 294px; color: var(--logo-blue); font-size: 50px; }
  .square-brand .brand-sub { font-size: 26px; margin-top: 6px; }

  .banner-brand { left: 660px; top: 42px; width: 238px; color: var(--logo-red); font-size: 42px; }
  .banner-brand .brand-sub { font-size: 22px; margin-top: 6px; }

  .hero-brand { left: 322px; top: 580px; width: 560px; color: var(--logo-red); font-size: 98px; }
  .hero-brand .brand-sub { font-size: 48px; margin-top: 12px; }

  .square-socials { position: absolute; left: 228px; top: 290px; list-style: none; color: var(--white); font-size: 22px; }
  .square-socials li { display: flex; align-items: center; height: 40.5px; }
  .square-socials .dot { width: 26px; height: 26px; background: var(--white); margin-right: 12px; }

  .placeholder-label { position: absolute; font-family: var(--sans); font-size: 42px; color: var(--ink); line-height: 1; }
  .text-label { left: 651px; top: 270px; }
  .picture-label { left: 926px; top: 254px; }

  .footer-socials { position: absolute; left: 0; top: 866px; width: 1200px; height: 42px; font-size: 34px; color: var(--ink); }
  .footer-socials .item { position: absolute; top: 0; display: flex; align-items: center; height: 42px; }
  .footer-socials .dot { width: 36px; height: 36px; background: var(--orange-deep); margin-right: 16px; }
</style>
</head>
<body>
<main class="canvas">
  <svg class="layer" width="1200" height="947" viewBox="0 0 1200 947" aria-hidden="true">
    <!-- square template -->
    <rect class="square-bg" x="70" y="0" width="494" height="494" fill="var(--orange-deep)"/>
    <rect class="square-frame" x="123" y="53" width="388" height="388" rx="22" fill="none" stroke="var(--white)" stroke-width="8"/>
    <polygon class="tilted-card" points="183,11 549,108 455,482 83,382" fill="var(--orange-deep)" stroke="var(--white)" stroke-width="8" stroke-linejoin="round"/>
    <polygon class="tilted-card-panel" points="243,236 509,280 455,482 91,382" fill="var(--orange-mid)" stroke="var(--white)" stroke-width="4" stroke-linejoin="round"/>

    <!-- banner template -->
    <polygon class="banner-shape" points="844,4 1126,4 1126,134 921,163 887,355 1124,487 1122,490 638,490 636,224 1062,82 844,8" fill="var(--orange-panel)" stroke="var(--orange-edge)" stroke-width="8" stroke-linejoin="miter"/>

    <!-- top stripe band -->
    <g class="stripe-band">
      <rect x="0" y="512" width="258" height="37" fill="var(--red)"/>
      <rect x="258" y="512" width="373" height="37" fill="var(--amber)"/>
      <rect x="631" y="512" width="114" height="37" fill="var(--orange-deep)"/>
      <rect x="745" y="512" width="183" height="37" fill="var(--red)"/>
      <rect x="928" y="512" width="272" height="37" fill="var(--tangerine)"/>
    </g>

    <!-- middle stripe -->
    <g class="stripe-band">
      <rect x="1" y="827" width="129" height="19" fill="var(--red)"/>
      <rect x="130" y="827" width="187" height="19" fill="var(--amber)"/>
      <rect x="317" y="827" width="56" height="19" fill="var(--orange-deep)"/>
      <rect x="373" y="827" width="92" height="19" fill="var(--red)"/>
      <rect x="465" y="827" width="271" height="19" fill="var(--tangerine)"/>
      <rect x="736" y="827" width="91" height="19" fill="var(--red)"/>
      <rect x="827" y="827" width="57" height="19" fill="var(--orange-deep)"/>
      <rect x="884" y="827" width="186" height="19" fill="var(--amber)"/>
      <rect x="1070" y="827" width="128" height="19" fill="var(--red)"/>
    </g>

    <!-- bottom stripe band -->
    <g class="stripe-band">
      <rect x="0" y="928" width="258" height="19" fill="var(--red)"/>
      <rect x="258" y="928" width="373" height="19" fill="var(--amber)"/>
      <rect x="631" y="928" width="114" height="19" fill="var(--orange-deep)"/>
      <rect x="745" y="928" width="183" height="19" fill="var(--red)"/>
      <rect x="928" y="928" width="272" height="19" fill="var(--tangerine)"/>
    </g>
  </svg>

  <div class="brand square-brand">TR Hornets<span class="brand-sub">Dunmore</span></div>
  <ul class="square-socials">
    <li><span class="dot"></span>@trhdunmore</li>
    <li><span class="dot"></span>TR Hornets Dunmore</li>
    <li><span class="dot"></span>@trhdunmore</li>
  </ul>

  <div class="brand banner-brand">TR Hornets<span class="brand-sub">Dunmore</span></div>
  <p class="placeholder-label text-label">Text Here</p>
  <p class="placeholder-label picture-label">Picture</p>

  <div class="brand hero-brand">TR Hornets<span class="brand-sub">Dunmore</span></div>

  <div class="footer-socials">
    <span class="item" style="left:95px"><span class="dot"></span>@trhdunmore</span>
    <span class="item" style="left:432px"><span class="dot"></span>TR Hornets Dunmore</span>
    <span class="item" style="left:855px"><span class="dot"></span>@trhdunmore</span>
  </div>
</main>
</body>
</html>
```